Cooking oil

To design a label for palm cooking oil (16,1x15,1cm). The brand is Vemara (logo enclosed). 20lit plastic container. The container colour is yellow and the cap colour is red.
Label background colour yellow.
Attached are examples to give an idea.

```html
<!DOCTYPE html>
<html lang="en">
<head>
<meta charset="UTF-8">
<title>Vemara Palm Olein Label</title>
<link rel="stylesheet" href="https://fonts.googleapis.com/css2?family=Jost:wght@400&family=Sacramento&family=Patua+One&display=swap">
<style>
  :root {
    --page-yellow: #c98a12;
    --label-cream: #f1f0e2;
    --label-pale-green: #dde9b4;
    --label-green: #a9d97c;
    --label-deep-green: #7cc35a;
    --leaf-green: #4f9a52;
    --brand-red: #d52f3c;
    --fruit-orange: #e8862a;
    --fruit-red: #d8442a;
  }
  * { margin: 0; padding: 0; box-sizing: border-box; }
  html, body {
    width: 1200px;
    height: 800px;
    overflow: hidden;
    background: var(--page-yellow);
  }
  .canvas {
    position: relative;
    width: 1200px;
    height: 800px;
  }
  .label {
    position: absolute;
    left: 290px;
    top: 82px;
    width: 620px;
    height: 636px;
    border-radius: 20px;
    overflow: hidden;
    background:
      linear-gradient(160deg,
        var(--label-cream) 0%,
        var(--label-cream) 18%,
        var(--label-pale-green) 30%,
        var(--label-cream) 40%,
        var(--label-pale-green) 55%,
        var(--label-green) 72%,
        var(--label-deep-green) 100%);
  }
  .corner-art {
    position: absolute;
    width: 66px;
    height: 100px;
    background: radial-gradient(circle at 0 50%, var(--leaf-green) 0%, rgba(79,154,82,0.55) 45%, rgba(79,154,82,0) 72%);
  }
  .corner-art--top-left { left: 0; top: 0; }
  .corner-art--top-right { right: 0; top: 0; transform: scaleX(-1); }
  .corner-art--bottom-left { left: 0; bottom: 0; }
  .corner-art--bottom-right { right: 0; bottom: 0; transform: scaleX(-1); }
  .brand {
    position: absolute;
    left: 0;
    right: 0;
    top: 112px;
    display: flex;
    align-items: center;
    justify-content: center;
    gap: 8px;
  }
  .brand-dot {
    width: 10px;
    height: 10px;
    border-radius: 50%;
    background: var(--brand-red);
  }
  .brand-name {
    font-family: "Patua One", serif;
    font-size: 32px;
    color: var(--brand-red);
    line-height: 1;
  }
  .product-title {
    position: absolute;
    left: 0;
    right: 0;
    top: 170px;
    text-align: center;
    color: var(--brand-red);
    font-weight: 400;
  }
  .product-title__script {
    display: block;
    font-family: "Sacramento", cursive;
    font-size: 132px;
    line-height: 130px;
    margin-left: 30px;
  }
  .product-title__caps {
    display: block;
    font-family: "Jost", sans-serif;
    font-size: 112px;
    line-height: 110px;
    white-space: nowrap;
    padding: 0 10px;
  }
  .fruit-art {
    position: absolute;
    left: 143px;
    top: 419px;
    width: 330px;
    height: 198px;
  }
</style>
</head>
<body>
<main class="canvas">
  <section class="label">
    <div class="corner-art corner-art--top-left" role="img" aria-label="Watercolour tropical leaf"></div>
    <div class="corner-art corner-art--top-right" role="img" aria-label="Watercolour tropical leaf"></div>
    <div class="corner-art corner-art--bottom-left" role="img" aria-label="Watercolour tropical leaf"></div>
    <div class="corner-art corner-art--bottom-right" role="img" aria-label="Watercolour tropical leaf"></div>

    <div class="brand">
      <span class="brand-dot"></span>
      <span class="brand-name">Vemara</span>
    </div>

    <h1 class="product-title">
      <span class="product-title__script">Palm</span>
      <span class="product-title__caps">OLEIN</span>
    </h1>

    <svg class="fruit-art" viewBox="0 0 330 198" role="img" aria-label="Watercolour illustration of palm fruits on palm fronds">
      <defs>
        <radialGradient id="fruitTone" cx="50%" cy="65%" r="55%">
          <stop offset="0%" stop-color="var(--fruit-orange)"/>
          <stop offset="55%" stop-color="var(--fruit-red)" stop-opacity="0.75"/>
          <stop offset="100%" stop-color="var(--leaf-green)" stop-opacity="0"/>
        </radialGradient>
      </defs>
      <rect x="0" y="0" width="330" height="198" fill="url(#fruitTone)"/>
    </svg>
  </section>
</main>
</body>
</html>
```